Brightfold Partners Website

Brightfold Partners (BP) provide Analytics & Enterprise Performance Management (EPM) advisory & consultancy services. We are passionate about data and making a difference for our clients by working in partnership with them, helping them on their journey to becoming an Brightfold Partner. We deliver insights which give our clients a competitive edge and a much deeper understanding of their organisation.

We need a website which shows who we are, what we do and how we do it.

www.brightfold-partners.example is our very basic website at the moment. We want to completely revamp it with a corporate look

```html
<!DOCTYPE html>
<html lang="en">
<head>
<meta charset="utf-8">
<title>Brightfold Partners</title>
<link rel="stylesheet" href="https://fonts.googleapis.com/css2?family=Lato:wght@700;900&family=Roboto:wght@300;400;500;700&display=swap">
<style>
:root{
  --navy:#274f6b;
  --navy-dark:#2c4e66;
  --orange:#e8692a;
  --orange-deep:#d9581c;
  --text:#7c7f84;
  --light:#f3f5f8;
  --white:#ffffff;
  --field:#ffffff;
  --line:#dfe3e8;
}
*{margin:0;padding:0;box-sizing:border-box}
html,body{width:1200px;height:3802px;overflow:hidden}
body{position:relative;font-family:'Roboto',sans-serif;color:var(--text);background:var(--white)}
.abs{position:absolute}
.heading-font{font-family:'Lato',sans-serif}

/* header & hero */
.hero{left:0;top:0;width:1200px;height:651px;background:linear-gradient(115deg,#3d5a6c 0%,#6b7a78 30%,#9a8f7d 55%,#b9a58c 70%,#6f7e7f 100%)}
.hero-shade{left:0;top:0;width:1200px;height:651px;background:linear-gradient(90deg,rgba(24,52,72,.72) 0%,rgba(24,52,72,.45) 45%,rgba(24,52,72,.05) 75%)}
.topbar{left:0;top:0;width:1200px;height:86px;background:rgba(39,79,107,.82)}
.brand{display:flex;align-items:center;gap:12px;color:var(--white);font-family:'Roboto',sans-serif;font-weight:700;letter-spacing:.5px;line-height:1.05}
.brand-dot{width:52px;height:52px;border-radius:50%;background:var(--white)}
.brand-name{font-size:20px;text-transform:uppercase}
.topbar .brand{left:111px;top:14px}
.utility{top:33px;left:768px;display:flex;align-items:center;gap:14px;color:var(--white);font-size:15px}
.utility .sep{opacity:.8}
.nav{top:106px;left:251px;width:700px;height:24px;color:var(--white);font-size:15px;font-weight:500}
.nav span{position:absolute;top:0;white-space:nowrap}
.nav .active::before{content:"";position:absolute;left:6px;top:-19px;width:30px;height:3px;background:var(--orange)}
.hero-title{left:251px;top:288px;font-size:40px;color:var(--white);font-family:'Lato',sans-serif;font-weight:700;letter-spacing:-.3px}
.hero-lead{left:253px;top:347px;width:450px;font-size:19px;line-height:29px;color:var(--white);font-weight:500}
.btn{display:flex;align-items:center;justify-content:center;background:var(--orange);color:var(--white);font-weight:700;font-size:15px;border-radius:30px;text-transform:uppercase}
.hero .btn{left:253px;top:428px;width:153px;height:47px}
.arrow-btn{width:40px;height:40px;border:2px solid rgba(255,255,255,.85);border-radius:50%;display:flex;align-items:center;justify-content:center}

/* who we are */
.who-frame{left:111px;top:790px;width:376px;height:438px;border:3px solid var(--orange)}
.who-photo{left:145px;top:754px;width:377px;height:442px;background:linear-gradient(160deg,#d9dde0 0%,#a9b2b3 35%,#7f8778 60%,#c0a58a 100%)}
.who-text{left:589px;top:864px;width:373px;font-size:15.5px;line-height:26.5px;font-weight:300;text-align:justify}
.who-text p+p{margin-top:18px}
.who-bar{left:1030px;top:754px;width:6px;height:154px;background:var(--orange)}
.who-title{left:1092px;top:754px;transform-origin:0 0;transform:rotate(90deg);font-family:'Lato',sans-serif;font-weight:900;font-size:46px;color:var(--navy);white-space:nowrap;line-height:41px}

/* what we do */
.services{left:0;top:1325px;width:1200px;height:1142px;background:var(--light)}
.section-title{width:1200px;left:0;text-align:center;font-family:'Lato',sans-serif;font-weight:900;font-size:50px;color:var(--navy);letter-spacing:-.5px}
.title-rule{left:540px;width:118px;height:4px;background:var(--orange)}
.service-title{font-family:'Lato',sans-serif;font-weight:700;font-size:25px;line-height:33px;color:var(--navy);text-transform:uppercase;letter-spacing:-.2px}
.service-copy{font-size:15.5px;line-height:26.5px;font-weight:300}
.service-copy p+p{margin-top:10px}
.service-photo-a{left:599px;top:1516px;width:490px;height:403px;border-radius:0 74px 0 74px;background:linear-gradient(140deg,#7d8e9c 0%,#c9c4b8 40%,#e2ddd3 65%,#57708a 100%)}
.service-photo-b{left:111px;top:1985px;width:488px;height:402px;border-radius:74px 0 74px 0;background:linear-gradient(120deg,#d6d8d7 0%,#bfa88b 35%,#cf8a3e 50%,#9a9896 70%,#e3e5e4 100%)}

/* how we do it */
.process{left:0;top:2467px;width:1200px;height:507px;background:linear-gradient(100deg,#d9601f 0%,#e6702e 35%,#dc6a2c 60%,#c95a22 100%)}
.process-title{left:111px;top:2879px;transform-origin:0 0;transform:rotate(-90deg);font-family:'Lato',sans-serif;font-weight:900;font-size:46px;color:var(--white);white-space:nowrap;line-height:41px}
.process-bar{left:159px;top:2723px;width:6px;height:152px;background:var(--white)}
.step{width:261px;color:var(--white)}
.step svg{display:block;height:46px;width:46px;margin-bottom:25px}
.step h3{font-family:'Roboto',sans-serif;font-weight:700;font-size:16.5px;margin-bottom:7px;text-transform:uppercase}
.step p{font-size:13.5px;line-height:24px;text-align:justify;font-weight:400}

/* contact */
.field{background:var(--field);border:1px solid var(--line);box-shadow:0 2px 8px rgba(0,0,0,.08);font-size:15px;color:#777;padding:15px 17px}
.send{left:511px;top:3326px;width:178px;height:47px;font-size:15px}

/* footer */
.footer{left:0;top:3458px;width:1200px;height:344px;background:var(--navy-dark)}
.footer .brand{left:111px;top:3584px}
.footer .brand-dot{width:62px;height:62px}
.footer .brand-name{font-size:23px;font-weight:500}
.f-head{font-size:17px;font-weight:500;color:var(--white);text-transform:uppercase}
.f-link{font-size:14.5px;color:var(--white);display:flex;align-items:center;gap:20px}
.f-link i{width:13px;height:13px;border-radius:50%;background:var(--orange);display:inline-block;position:relative}
.f-link i::after{content:"";position:absolute;left:3px;top:4px;width:4px;height:4px;border-top:1.5px solid var(--navy-dark);border-right:1.5px solid var(--navy-dark);transform:rotate(45deg)}
.f-label{font-size:14px;font-weight:500;color:var(--white);text-transform:uppercase}
.f-small{font-size:12px;color:var(--white);line-height:24px}
.news{left:788px;top:3550px;width:300px;height:50px;border-radius:26px;background:var(--white);border:2px solid #cfd6dc}
.news span{position:absolute;left:17px;top:14px;font-size:14.5px;color:#555}
.news .btn{position:absolute;right:3px;top:3px;width:105px;height:40px;font-size:15px}
.social{width:36px;height:36px;border-radius:50%;background:var(--white)}
.footer-rule{left:111px;top:3739px;width:978px;height:1px;background:rgba(255,255,255,.25)}
.copyright{left:0;top:3757px;width:1200px;text-align:center;font-size:12.5px;color:var(--white)}
</style>
</head>
<body>

<!-- hero -->
<div class="abs hero" role="img" aria-label="Smiling young professional with glasses using a phone in a busy open-plan office with colleagues at a table"></div>
<div class="abs hero-shade"></div>
<div class="abs topbar"></div>
<div class="abs brand"><span class="brand-dot"></span><span class="brand-name">Brightfold<br>Partners</span></div>
<div class="abs utility">
  <svg width="16" height="16" viewBox="0 0 16 16"><circle cx="6.5" cy="6.5" r="4.8" fill="none" stroke="#fff" stroke-width="2"/><path d="M10 10l4.5 4.5" stroke="#fff" stroke-width="2.4" stroke-linecap="round"/></svg>
  <span>01 555 0142</span><span class="sep">|</span><span>CONTACT US</span><span class="sep">|</span><span>LOGIN</span>
</div>
<nav class="abs nav">
  <span class="active" style="left:0">HOME</span>
  <span style="left:114px">WHO WE ARE</span>
  <span style="left:276px">WHAT WE DO</span>
  <span style="left:440px">HOW WE DO IT</span>
  <span style="left:611px">RESOURCES</span>
</nav>
<h1 class="abs hero-title">BRIGHTFOLD PARTNERS</h1>
<p class="abs hero-lead">Brightfold Partners is an exciting start-up in the Data Analytics and EPM space.</p>
<div class="hero"></div>
<a class="abs btn" style="left:253px;top:428px;width:153px;height:47px">Learn More</a>
<div class="abs arrow-btn" style="left:990px;top:547px"><svg width="12" height="16" viewBox="0 0 12 16"><path d="M8 2L3 8l5 6" fill="none" stroke="#fff" stroke-width="2"/></svg></div>
<div class="abs arrow-btn" style="left:1047px;top:547px"><svg width="12" height="16" viewBox="0 0 12 16"><path d="M4 2l5 6-5 6" fill="none" stroke="#fff" stroke-width="2"/></svg></div>

<!-- who we are -->
<div class="abs who-frame"></div>
<div class="abs who-photo" role="img" aria-label="Businesswoman presenting sticky notes on a board to seated colleagues in a bright office"></div>
<div class="abs who-text">
  <p>Brightfold Partners is an exciting start-up in the Data Analytics and EPM space. &nbsp;Founded in 2019, BP specialise in the implementation and support of BI, EPM and Data Analytics business solutions, both in the Cloud and on-premise.</p>
  <p>BP are a Data Analytics &amp; EPM company, specialising in the implementation and support of Business Intelligence, EPM and Data Analytics business solutions, both in the Cloud and on-premise.</p>
</div>
<div class="abs who-bar"></div>
<h2 class="abs who-title">WHO WE ARE</h2>

<!-- what we do -->
<div class="abs services"></div>
<h2 class="abs section-title" style="top:1392px">WHAT WE DO</h2>
<div class="abs title-rule" style="top:1456px"></div>

<h3 class="abs service-title" style="left:111px;top:1532px;width:420px">Analytics &amp; Enterprise<br>Performance Management</h3>
<div class="abs service-copy" style="left:111px;top:1618px;width:412px">
  <p>Lorem ipsum dolor sit amet, consectetur adipiscing elit, sed do eiusmod tempor incididunt ut labore et dolore magna aliqua. Ut enim ad minim veniam, quis nostrud exercitation ullamco laboris nisi ut aliquip.</p>
  <p>Tempor incididunt ut labore et dolore magna aliqua. Ut enim ad minim veniam, quis nostrud exercitation ullamco laboris nisi ut aliquip ex ea commodo consequat.</p>
</div>
<a class="abs btn" style="left:111px;top:1847px;width:155px;height:48px">Learn More</a>
<div class="abs service-photo-a" role="img" aria-label="Overhead view of a business team reviewing charts and laptops around a meeting table"></div>

<div class="abs service-photo-b" role="img" aria-label="Three colleagues meeting on a sofa around a table with a laptop in a modern office"></div>
<h3 class="abs service-title" style="left:677px;top:2000px;width:420px">Advisory and<br>Consultancy Services</h3>
<div class="abs service-copy" style="left:677px;top:2086px;width:412px">
  <p>Lorem ipsum dolor sit amet, consectetur adipiscing elit, sed do eiusmod tempor incididunt ut labore et dolore magna aliqua. Ut enim ad minim veniam, quis nostrud exercitation ullamco laboris nisi ut aliquip.</p>
  <p>Tempor incididunt ut labore et dolore magna aliqua. Ut enim ad minim veniam, quis nostrud exercitation ullamco laboris nisi ut aliquip ex ea commodo consequat.</p>
</div>
<a class="abs btn" style="left:677px;top:2315px;width:155px;height:48px">Learn More</a>

<!-- how we do it -->
<div class="abs process" role="img" aria-label="Orange-tinted photo of a team working at desks"></div>
<div class="abs process-bar"></div>
<h2 class="abs process-title">HOW WE DO IT</h2>

<div class="abs step" style="left:227px;top:2539px">
  <svg viewBox="0 0 46 46" fill="none" stroke="#fff" stroke-width="1.8"><rect x="3" y="5" width="40" height="36"/><path d="M3 12h40M10 36V26M17 36V20M24 36V24M31 36V17M38 36V22"/><path d="M8 22l9-6 7 4 12-8"/></svg>
  <h3>Sed ut perspicia</h3>
  <p>Lorem ipsum dolor sit amet, consectetur adipiscing elit, sed do eiusmod tempor incididunt ut laborea.</p>
</div>
<div class="abs step" style="left:527px;top:2539px">
  <svg viewBox="0 0 46 46" fill="none" stroke="#fff" stroke-width="1.8"><circle cx="23" cy="20" r="9"/><circle cx="23" cy="20" r="3.5"/><path d="M23 5v5M23 30v5M8 20h5M33 20h5M12.5 9.5l3.5 3.5M30 27l3.5 3.5M33.5 9.5L30 13M16 27l-3.5 3.5"/><path d="M10 38c4 4 22 4 26 0"/></svg>
  <h3>Sed ut perspicia</h3>
  <p>Lorem ipsum dolor sit amet, consectetur adipiscing elit, sed do eiusmod tempor incididunt ut laborea.</p>
</div>
<div class="abs step" style="left:828px;top:2539px">
  <svg viewBox="0 0 46 46" fill="none" stroke="#fff" stroke-width="1.8"><rect x="4" y="18" width="14" height="25"/><rect x="18" y="6" width="12" height="37"/><rect x="30" y="13" width="12" height="30"/><path d="M8 23h6M8 29h6M8 35h6M22 11h4M22 17h4M22 23h4M22 29h4M34 18h4M34 24h4M34 30h4M2 43h42"/></svg>
  <h3>Sed ut perspicia</h3>
  <p>Lorem ipsum dolor sit amet, consectetur adipiscing elit, sed do eiusmod tempor incididunt ut laborea.</p>
</div>
<div class="abs step" style="left:227px;top:2738px">
  <svg viewBox="0 0 46 46" fill="none" stroke="#fff" stroke-width="1.8"><circle cx="20" cy="10" r="5"/><path d="M11 30v-8c0-4 4-6 9-6s9 2 9 6v8"/><path d="M4 30h38M8 30v13M38 30v13"/><rect x="28" y="20" width="12" height="10"/></svg>
  <h3>Sed ut perspicia</h3>
  <p>Lorem ipsum dolor sit amet, consectetur adipiscing elit, sed do eiusmod tempor incididunt ut laborea.</p>
</div>
<div class="abs step" style="left:527px;top:2738px">
  <svg viewBox="0 0 46 46" fill="none" stroke="#fff" stroke-width="1.8"><circle cx="15" cy="20" r="6"/><path d="M4 42c0-8 5-12 11-12s11 4 11 12"/><rect x="26" y="3" width="16" height="16"/><path d="M34 7v8M31 9h5M31 13h5"/><path d="M28 42v-8M33 42v-12M38 42v-16"/></svg>
  <h3>Sed ut perspicia</h3>
  <p>Lorem ipsum dolor sit amet, consectetur adipiscing elit, sed do eiusmod tempor incididunt ut laborea.</p>
</div>
<div class="abs step" style="left:828px;top:2738px">
  <svg viewBox="0 0 46 46" fill="none" stroke="#fff" stroke-width="1.8"><path d="M14 26a10 10 0 1 1 14 0v6H14z"/><path d="M16 36h10M18 40h6"/><path d="M21 5V1M8 12l-3-2M34 12l3-2M5 22H1M41 22h4"/><path d="M21 16v8M17 20h8"/></svg>
  <h3>Sed ut perspicia</h3>
  <p>Lorem ipsum dolor sit amet, consectetur adipiscing elit, sed do eiusmod tempor incididunt ut laborea.</p>
</div>

<!-- get in touch -->
<h2 class="abs section-title" style="top:3048px">GET IN TOUCH</h2>
<div class="abs title-rule" style="top:3112px"></div>
<div class="abs field" style="left:139px;top:3153px;width:299px;height:48px">Full Name</div>
<div class="abs field" style="left:449px;top:3153px;width:299px;height:48px">Phone</div>
<div class="abs field" style="left:759px;top:3153px;width:300px;height:48px">Email Address</div>
<div class="abs field" style="left:139px;top:3214px;width:921px;height:93px">Message</div>
<a class="abs btn send">Send Message</a>

<!-- footer -->
<footer class="abs footer"></footer>
<div class="abs brand" style="left:111px;top:3585px"><span class="brand-dot" style="width:62px;height:62px"></span><span class="brand-name" style="font-size:23px">Brightfold<br>Partners</span></div>

<div class="abs f-head" style="left:384px;top:3505px">Quick Links</div>
<div class="abs f-link" style="left:384px;top:3547px"><i></i>Home</div>
<div class="abs f-link" style="left:384px;top:3581px"><i></i>Who We Are</div>
<div class="abs f-link" style="left:384px;top:3616px"><i></i>What We Do</div>
<div class="abs f-link" style="left:384px;top:3650px"><i></i>How We Do It</div>
<div class="abs f-link" style="left:384px;top:3684px"><i></i>Resources</div>

<div class="abs f-head" style="left:554px;top:3505px">Contact Info</div>
<svg class="abs" style="left:553px;top:3547px" width="12" height="15" viewBox="0 0 12 15"><path d="M6 14C2 9 1 7 1 5.5a5 5 0 0 1 10 0C11 7 10 9 6 14z" fill="#e8692a"/><circle cx="6" cy="5.5" r="1.8" fill="#2c4e66"/></svg>
<div class="abs f-label" style="left:587px;top:3548px">Address:</div>
<div class="abs f-small" style="left:587px;top:3566px">12 Harbour Row,<br>Quay District, Dublin 9, D09 XK41</div>
<svg class="abs" style="left:553px;top:3624px" width="14" height="14" viewBox="0 0 14 14"><path d="M3 1l3 3-1.6 1.8c.8 1.7 2.2 3.1 3.8 3.8L10 8l3 3-1.8 2C6 13 1 8 1 2.8z" fill="#e8692a"/></svg>
<div class="abs f-label" style="left:587px;top:3622px">Phone:</div>
<div class="abs f-small" style="left:587px;top:3643px">01 555 0142</div>
<svg class="abs" style="left:553px;top:3680px" width="15" height="11" viewBox="0 0 15 11"><rect width="15" height="11" fill="#e8692a"/><path d="M0 0l7.5 6L15 0" fill="none" stroke="#2c4e66" stroke-width="1.4"/></svg>
<div class="abs f-label" style="left:587px;top:3677px">Email:</div>
<div class="abs f-small" style="left:587px;top:3697px">info@brightfold-partners.example</div>

<div class="abs f-head" style="left:787px;top:3505px">Newsletter Signup</div>
<div class="abs news"><span>Email Address</span><a class="btn">Sign Up</a></div>
<div class="abs social" style="left:788px;top:3616px;background:var(--orange)"></div>
<div class="abs social" style="left:829px;top:3616px"></div>
<div class="abs social" style="left:869px;top:3616px"></div>
<div class="abs social" style="left:909px;top:3616px"></div>

<div class="abs footer-rule"></div>
<div class="abs copyright">© 2022 BRIGHTFOLD PARTNERS &nbsp;/ &nbsp;All Rights Reserved</div>

</body>
</html>
```